ALL TEXT GRAPHICS TM May 2025 for Instagram

We are looking for a series of social media graphics for Instagram (new size: 4:5 (1080 x 1350 pixels) ratio that are ALL TEXT. We want the following quotes below on each graphic; one quote per graphic. AND, In very small letters at the bottom of each graphic, add @TovaMarshOnline
The look and feel of these graphics should be complimentary to the color palette attached below; but keep them simple. But the design is up to you; at the end of this document, I provided various samples of all text graphics that I like as examples.
Target Market(s)
women looking to lose weight
Look and feel

```html
<!DOCTYPE html>
<html lang="en">
<head>
<meta charset="utf-8">
<title>All Text Graphics – Tova Marsh</title>
<link rel="stylesheet" href="https://fonts.googleapis.com/css2?family=Anton&family=DM+Serif+Display:ital@0;1&family=Fredoka:wght@500;600;700&family=Great+Vibes&family=Oswald:wght@400;500;600;700&family=Playfair+Display:ital,wght@0,700;0,800;0,900;1,700&family=Poppins:ital,wght@0,400;0,500;0,600;0,700;0,800;1,400;1,600;1,700;1,800&display=swap">
<style>
:root{
  --bg:#d4d5d8;
  --paper:#ffffff;
  --hot:#ec0a7f;
  --deep:#d6006b;
  --rose:#d4246b;
  --soft:#f07ab4;
  --blush:#ee6aa7;
  --maroon:#b32c57;
  --ink:#1d1d1f;
}
*{margin:0;padding:0;box-sizing:border-box}
html,body{width:1200px;height:624px;overflow:hidden;background:var(--bg)}
.sheet{position:relative;width:1200px;height:624px}
.card{position:absolute;width:211px;height:264px;background:var(--paper);box-shadow:6px 8px 14px rgba(0,0,0,.18);overflow:hidden}
.row-1{top:38px}.row-2{top:322px}
.col-1{left:30px}.col-2{left:262px}.col-3{left:494px}.col-4{left:726px}.col-5{left:958px}
.t{position:absolute;left:0;right:0;text-align:center;white-space:nowrap;line-height:1}
.handle{font-family:"Great Vibes",cursive;font-size:13px;color:var(--ink)}
.band{position:absolute;left:0;right:0;color:#fff;display:flex;align-items:center;justify-content:center;white-space:nowrap}
.rule{position:absolute;height:2px;background:var(--hot)}
.shape{position:absolute}

/* card 1 */
.c1 .head{left:22px;right:auto;text-align:left;font-family:"Playfair Display",serif;font-weight:800;font-size:34px;letter-spacing:-1.4px}
.c1 .sub{font-family:"Poppins",sans-serif;font-size:11.5px;color:var(--ink);line-height:1.25;left:12px}
.c1 .band{top:192px;height:31px;background:var(--deep);font-family:"Poppins",sans-serif;font-weight:700;font-size:17px}

/* card 2 */
.c2 .big{font-family:"Anton",sans-serif;color:var(--deep)}
.c2 .band{top:107px;height:23px;background:var(--blush);font-family:"Oswald",sans-serif;font-weight:600;font-size:16px;letter-spacing:.5px}
.c2 .body{font-family:"Oswald",sans-serif;font-weight:500;font-size:15.5px;color:var(--ink);line-height:1.08}

/* card 3 */
.c3 .your{font-family:"Great Vibes",cursive;font-size:40px;color:var(--soft);top:10px}
.c3 .belly{font-family:"Anton",sans-serif;font-size:60px;color:var(--hot);top:42px;letter-spacing:1px}
.c3 .fat{font-family:"Anton",sans-serif;font-size:37px;top:107px;color:var(--hot);letter-spacing:.5px}
.c3 .fat span{color:var(--soft)}
.c3 .band{top:184px;height:22px;background:var(--hot);font-family:"Oswald",sans-serif;font-weight:600;font-size:16px}

/* card 4 */
.c4 .soft{font-family:"Fredoka",sans-serif;font-weight:600;color:var(--deep)}
.c4 .forty{font-family:"Poppins",sans-serif;font-weight:800;font-size:76px;color:var(--hot);top:96px;letter-spacing:-2px}
.c4 .note{font-family:"Oswald",sans-serif;font-weight:500;font-size:11px;color:var(--ink);line-height:1.15}
.c4 .note b{color:var(--hot);font-weight:500}

/* card 5 */
.c5 .flat{font-family:"Fredoka",sans-serif;font-weight:700;color:var(--hot)}
.c5 .band{top:183px;height:24px;background:var(--hot);font-family:"Poppins",sans-serif;font-weight:600;font-size:13.5px}

/* card 6 */
.c6 .head{left:16px;right:auto;text-align:left;font-family:"Playfair Display",serif;font-weight:800;font-size:33px;letter-spacing:-1.2px}

/* card 7 */
.c7 .it{font-family:"Poppins",sans-serif;font-style:italic;color:var(--hot)}
.c7 .band{top:194px;height:24px;background:var(--deep);font-family:"Oswald",sans-serif;font-weight:500;font-size:14px}

/* card 8 */
.c8 .list{position:absolute;left:40px;top:143px;font-family:"DM Serif Display",serif;font-size:17px;color:var(--ink);line-height:21px}
.c8 .list li{list-style:none;display:flex;align-items:center;gap:7px}
.c8 .band{top:114px;height:22px;background:var(--maroon);font-family:"Poppins",sans-serif;font-weight:600;font-size:12.5px}

/* card 9 */
.c9 .l{left:14px;right:auto;text-align:left;font-family:"Oswald",sans-serif;font-weight:600}

/* card 10 */
.c10 .band{top:97px;height:22px;background:var(--rose);font-family:"Oswald",sans-serif;font-weight:600;font-size:15.5px}
</style>
</head>
<body>
<main class="sheet">

  <!-- 1 -->
  <section class="card c1 row-1 col-1">
    <p class="t head" style="top:18px;color:var(--soft)">Tired.</p>
    <p class="t head" style="top:51px;color:var(--deep)">Moody.</p>
    <p class="t head" style="top:84px;color:var(--deep)">Stubborn</p>
    <p class="t head" style="top:117px;color:var(--ink)">Belly Fat.</p>
    <p class="t sub" style="top:159px">YOUR <b>HORMONES</b> ARE<br>SCREAMING FOR HELP!</p>
    <div class="band">LET'S FIX THAT!</div>
    <p class="t handle" style="top:232px">@TovaMarshOnline</p>
  </section>

  <!-- 2 -->
  <section class="card c2 row-1 col-2">
    <p class="t big" style="top:21px;font-size:26px">THAT STUBBORN</p>
    <p class="t big" style="top:47px;font-size:50px">WEIGHT?</p>
    <div class="band">IT'S NOT YOUR FAULT.</div>
    <p class="t body" style="top:139px">Your Hormones<br>are to Blame and<br>You're Not Alone;</p>
    <p class="t body" style="top:192px;color:var(--deep);font-size:19px">But there is a Fix.</p>
    <div class="rule" style="left:75px;width:62px;top:218px;background:var(--blush)"></div>
    <p class="t handle" style="top:229px">@TovaMarshOnline</p>
  </section>

  <!-- 3 -->
  <section class="card c3 row-1 col-3">
    <p class="t your">Your</p>
    <p class="t belly">BELLY</p>
    <p class="t fat"><span>ISN'T</span> FAT...</p>
    <p class="t" style="top:148px;font-family:'Poppins',sans-serif;font-weight:600;font-size:10.5px;letter-spacing:1.3px;color:var(--ink)">IT'S HORMONAL.</p>
    <div class="rule" style="left:0;width:40px;top:172px"></div>
    <div class="rule" style="right:0;width:40px;top:172px"></div>
    <p class="t" style="top:166px;font-family:'Oswald',sans-serif;font-weight:500;font-size:13px;color:var(--hot)">And here's how to fix it.</p>
    <div class="band">Comment HORMONES</div>
    <p class="t" style="top:211px;font-family:'DM Serif Display',serif;font-size:15px;color:var(--ink)">if nothing is working.</p>
    <p class="t handle" style="top:235px">@TovaMarshOnline</p>
  </section>

  <!-- 4 -->
  <section class="card c4 row-1 col-4">
    <p class="t soft" style="top:17px;font-size:23px">The Stubborn</p>
    <p class="t soft" style="top:39px;font-size:42px;letter-spacing:-.5px">Belly Fat</p>
    <div class="rule" style="left:33px;width:45px;top:90px"></div>
    <div class="rule" style="right:33px;width:45px;top:90px"></div>
    <p class="t soft" style="top:82px;font-size:17px;color:var(--hot);font-family:'Poppins',sans-serif;font-weight:700">after</p>
    <p class="t forty">40?</p>
    <p class="t note" style="top:175px">It's not about <b>CALORIES;</b><br>it's about your <b>HORMONES.</b></p>
    <svg class="shape" style="left:35px;top:204px" width="142" height="26" viewBox="0 0 142 26"><polygon points="0,0 142,0 134,13 142,26 0,26 8,13" fill="var(--hot)"/></svg>
    <p class="t" style="top:206px;font-family:'Oswald',sans-serif;font-weight:600;font-size:18px;color:#fff">Here is the Fix!</p>
    <p class="t handle" style="top:237px">@TovaMarshOnline</p>
  </section>

  <!-- 5 -->
  <section class="card c5 row-1 col-5">
    <p class="t flat" style="top:12px;font-size:58px;letter-spacing:2px">FLAT</p>
    <p class="t flat" style="top:66px;font-size:37px;color:var(--deep)">TUMMY</p>
    <div class="rule" style="left:35px;width:42px;top:113px"></div>
    <div class="rule" style="right:35px;width:42px;top:113px"></div>
    <p class="t" style="top:106px;font-family:'Poppins',sans-serif;font-size:13px;color:var(--ink)">in your</p>
    <p class="t" style="top:118px;font-family:'Poppins',sans-serif;font-weight:800;font-size:40px;letter-spacing:4px;color:#2e2e30">40s?</p>
    <p class="t" style="top:164px;font-family:'Poppins',sans-serif;font-style:italic;font-weight:700;font-size:13px;color:var(--hot)">It's still Possible!</p>
    <div class="band">Comment BYE BELLY</div>
    <p class="t" style="top:214px;font-family:'Poppins',sans-serif;font-style:italic;font-size:9px;color:var(--ink);line-height:1.05">To get the 10 secrets to<br><b>A FLATTER TUMMY</b></p>
    <p class="t handle" style="top:240px">@TovaMarshOnline</p>
  </section>

  <!-- 6 -->
  <section class="card c6 row-2 col-1">
    <p class="t head" style="top:20px;color:var(--soft)">Bloating</p>
    <p class="t head" style="top:55px;color:var(--hot)">Muffin Top.</p>
    <p class="t head" style="top:88px;color:var(--deep)">Puffy</p>
    <p class="t head" style="top:120px;color:var(--ink)">Waistline.</p>
    <p class="t" style="top:156px;left:26px;right:auto;text-align:left;font-family:'Poppins',sans-serif;font-style:italic;font-size:10px;color:var(--ink)">Your body's screaming for</p>
    <p class="t" style="top:167px;left:26px;right:auto;text-align:left;font-family:'Poppins',sans-serif;font-weight:600;font-size:10.5px;color:var(--ink)">a different kind of fix.</p>
    <svg class="shape" style="left:19px;top:184px" width="172" height="50" viewBox="0 0 172 50"><polygon points="0,0 172,0 160,15 172,30 0,30 12,15" fill="var(--rose)"/><polygon points="6,34 90,34 12,48" fill="var(--hot)"/></svg>
    <p class="t" style="top:188px;font-family:'Poppins',sans-serif;font-weight:700;font-size:21px;color:#fff;left:-10px">Here it is!</p>
    <p class="t handle" style="top:229px;left:auto;right:20px;text-align:right">@TovaMarshOnline</p>
  </section>

  <!-- 7 -->
  <section class="card c7 row-2 col-2">
    <p class="t it" style="top:25px;font-size:14px;font-weight:600">You're doing all the</p>
    <p class="t it" style="top:42px;font-size:22px;font-weight:800">“Right” things,</p>
    <div class="rule" style="left:28px;width:40px;top:75px;background:var(--deep)"></div>
    <div class="rule" style="right:28px;width:40px;top:75px;background:var(--deep)"></div>
    <p class="t" style="top:68px;font-family:'Poppins',sans-serif;font-style:italic;font-weight:600;font-size:13px;color:var(--ink)">but your</p>
    <p class="t" style="top:84px;font-family:'Anton',sans-serif;font-size:66px;color:var(--deep);letter-spacing:1px">BELLY</p>
    <p class="t" style="top:156px;font-family:'Oswald',sans-serif;font-weight:600;font-size:22px;color:var(--ink)">won't go down?</p>
    <svg class="shape" style="left:0;top:175px" width="211" height="68" viewBox="0 0 211 68"><polygon points="150,16 211,4 211,16" fill="var(--blush)"/><polygon points="0,50 80,50 0,66" fill="var(--blush)"/></svg>
    <div class="band">HERE'S what you haven't tried.</div>
    <p class="t handle" style="top:229px;left:auto;right:34px;text-align:right">@TovaMarshOnline</p>
  </section>

  <!-- 8 -->
  <section class="card c8 row-2 col-3">
    <p class="t" style="top:12px;left:70px;right:auto;font-family:'Great Vibes',cursive;font-size:40px;color:var(--soft)">This</p>
    <p class="t" style="top:30px;left:44px;right:auto;font-family:'Playfair Display',serif;font-weight:900;font-size:84px;color:var(--rose);letter-spacing:-5px">90</p>
    <svg class="shape" style="left:134px;top:47px" width="48" height="48" viewBox="0 0 48 48"><circle cx="24" cy="24" r="23" fill="var(--soft)"/></svg>
    <p class="t" style="top:57px;left:134px;right:auto;width:48px;font-family:'DM Serif Display',serif;font-size:13px;color:#fff;line-height:.95;transform:rotate(-12deg)">Day<br>Plan</p>
    <div class="band">helped women&nbsp;<span style="color:#f5a3c8">over 40</span></div>
    <ul class="list">
      <li><svg width="12" height="12" viewBox="0 0 12 12"><circle cx="6" cy="6" r="5" fill="none" stroke="var(--hot)" stroke-width="1"/><path d="M3.3 6.2 5.3 8 9 4" fill="none" stroke="var(--hot)" stroke-width="1.4"/></svg>Slim Down,</li>
      <li><svg width="12" height="12" viewBox="0 0 12 12"><circle cx="6" cy="6" r="5" fill="none" stroke="var(--hot)" stroke-width="1"/><path d="M3.3 6.2 5.3 8 9 4" fill="none" stroke="var(--hot)" stroke-width="1.4"/></svg>Get a Tiny Waist</li>
      <li><svg width="12" height="12" viewBox="0 0 12 12"><circle cx="6" cy="6" r="5" fill="none" stroke="var(--hot)" stroke-width="1"/><path d="M3.3 6.2 5.3 8 9 4" fill="none" stroke="var(--hot)" stroke-width="1.4"/></svg>feel sexy again.</li>
    </ul>
    <p class="t" style="top:208px;font-family:'DM Serif Display',serif;font-style:italic;font-size:20px;color:var(--hot)">You're next.</p>
    <p class="t handle" style="top:235px">@TovaMarshOnline</p>
  </section>

  <!-- 9 -->
  <section class="card c9 row-2 col-4">
    <p class="t l" style="top:16px;font-size:24px;color:var(--rose)">This is the</p>
    <p class="t l" style="top:42px;font-family:'Anton',sans-serif;font-size:54px;color:var(--rose);letter-spacing:.5px">SECRET</p>
    <p class="t l" style="top:94px;font-size:20px;color:var(--ink)">Women <span style="color:var(--rose)">Over 40</span></p>
    <p class="t l" style="top:115px;font-size:19px;color:var(--rose)">are using to get</p>
    <p class="t l" style="top:136px;font-size:25px;color:var(--hot)">SNATCHED;</p>
    <p class="t l" style="top:162px;left:18px;font-size:19px;color:var(--ink)">Without Starving.</p>
    <svg class="shape" style="left:0;top:162px" width="211" height="44" viewBox="0 0 211 44"><polygon points="160,18 211,2 211,18" fill="var(--hot)"/><g fill="var(--hot)"><polygon points="153,18 159,18 166,4 160,4"/><polygon points="144,18 150,18 157,4 151,4"/></g><polygon points="0,26 38,26 33,42 0,42" fill="var(--hot)"/><g fill="var(--hot)"><polygon points="40,42 46,42 53,26 47,26"/><polygon points="50,42 56,42 63,26 57,26"/><polygon points="60,42 66,42 73,26 67,26"/></g></svg>
    <p class="t" style="top:188px;left:75px;right:auto;font-family:'DM Serif Display',serif;font-style:italic;font-size:15px;color:var(--ink)">Comment SKINNY</p>
    <p class="t" style="top:215px;font-family:'Oswald',sans-serif;font-weight:500;font-size:13px;color:var(--ink)">to get the exact plan.</p>
    <p class="t handle" style="top:235px">@TovaMarshOnline</p>
  </section>

  <!-- 10 -->
  <section class="card c10 row-2 col-5">
    <p class="t" style="top:18px;font-family:'Playfair Display',serif;font-weight:800;font-size:23px;line-height:1;color:var(--rose);letter-spacing:-.8px;transform:scaleX(.92)">What Worked In<br>Your 30s Won't<br>Work Now.</p>
    <div class="band">Here's what actually does !</div>
    <div class="rule" style="left:25px;width:40px;top:142px;height:1px;background:var(--rose)"></div>
    <div class="rule" style="left:25px;width:40px;top:167px;height:1px;background:var(--rose)"></div>
    <div class="rule" style="right:22px;width:60px;top:142px;height:1px;background:var(--rose)"></div>
    <div class="rule" style="right:22px;width:60px;top:167px;height:1px;background:var(--rose)"></div>
    <p class="t" style="top:143px;left:25px;right:auto;font-family:'Oswald',sans-serif;font-weight:600;font-size:21px;color:var(--rose)">Drop</p>
    <p class="t" style="top:124px;font-family:'Anton',sans-serif;font-size:58px;color:var(--blush);left:-6px">30</p>
    <p class="t" style="top:143px;left:auto;right:22px;font-family:'Oswald',sans-serif;font-weight:600;font-size:21px;color:var(--rose)">Pounds</p>
    <p class="t" style="top:190px;font-family:'Oswald',sans-serif;font-weight:600;font-size:25px;color:var(--ink)">in 3 Months.</p>
    <p class="t handle" style="top:232px">@TovaMarshOnline</p>
  </section>

</main>
</body>
</html>
```